Book Cover For Social Media Project

I am requiring a book cover for my upcoming book “Folding Waves Toward Harvests”

This book is for Network Marketers wanting to build their business on Social Media. Helping them get business from likes they receive on Chatterloom.

The book design needs to be clear that it is a business book that is all about social media is a fun, modern way.

Target Market(s)

Men and Women aged 18-65 wanting to make money from their social media accounts.

Industry/Entity Type

Business

Colors

Designer to choose colors to be used in the design.

Requirements
Must have
• Clear and obvious relationship to social media and business.
• The title “Folding Waves Toward Harvests”
• Author name “Dorian Halvette”
• Tag line “A Complete Handbook For Growing Your Direct Selling Venture Through Online Channels”
Nice to have
• Emojis that are used on Chatterloom.

```html
<!DOCTYPE html>
<html lang="en">
<head>
<meta charset="utf-8">
<title>Folding Waves Toward Harvests — Book Cover Wrap</title>
<link rel="stylesheet" href="https://fonts.googleapis.com/css2?family=Anton&family=Montserrat:wght@500;700&family=Raleway:wght@400;500&display=swap">
<style>
  :root {
    --bg: #e3e3e3;
    --paper: #ffffff;
    --brand-blue: #2f4f8f;
    --ink: #2b2b2b;
    --tag-gray: #6f6f6f;
    --crowd-warm: #c9a894;
    --crowd-cool: #b8bfc9;
    --photo-tone: #9aa4b3;
  }
  * { box-sizing: border-box; margin: 0; padding: 0; }
  html, body { width: 1200px; height: 1200px; overflow: hidden; background: var(--bg); }
  .wrap {
    position: absolute; left: 53px; top: 188px;
    width: 1094px; height: 824px;
    background: var(--paper);
  }
  .back-cover { position: absolute; left: 0; top: 0; width: 536px; height: 100%; }
  .spine {
    position: absolute; left: 536px; top: 0; width: 22px; height: 100%;
    background: var(--brand-blue);
  }
  .front-cover { position: absolute; left: 558px; top: 0; width: 536px; height: 100%; }

  /* Back cover */
  .back-mark {
    position: absolute; left: 350px; top: 62px; width: 84px; height: 80px;
    border-radius: 18px;
    background: radial-gradient(circle at 50% 50%, var(--crowd-warm), var(--crowd-cool) 70%, transparent 72%);
  }
  .back-title {
    position: absolute; left: 96px; top: 50px; width: 280px;
    font-family: "Anton", sans-serif; color: var(--brand-blue);
    font-size: 33px; line-height: 44px; text-transform: uppercase; text-align: center;
    white-space: nowrap;
  }
  .back-tagline {
    position: absolute; left: 90px; top: 143px; width: 340px;
    font-family: "Montserrat", sans-serif; font-weight: 700; font-size: 7.6px;
    line-height: 10px; color: var(--brand-blue); text-transform: uppercase; text-align: center;
  }
  .blurb {
    position: absolute; left: 50px; top: 188px; width: 440px;
    font-family: "Raleway", sans-serif; font-size: 13.4px; line-height: 18.7px;
    color: var(--ink); text-align: center;
  }
  .blurb p + p { margin-top: 18px; }
  .about-heading {
    position: absolute; left: 180px; top: 428px; width: 280px;
    font-family: "Anton", sans-serif; font-size: 26px; color: var(--brand-blue);
    text-transform: uppercase; text-align: center; letter-spacing: 0.5px;
  }
  .author-bio {
    position: absolute; left: 51px; top: 466px; width: 440px;
    font-family: "Raleway", sans-serif; font-size: 13.4px; line-height: 18.7px; color: var(--ink);
  }
  .author-photo {
    float: left; width: 118px; height: 133px; margin: -28px 10px 4px 7px;
    background: linear-gradient(160deg, #c7ccd4, var(--photo-tone) 70%, #6d7b92);
  }
  .author-bio .name {
    font-family: "Montserrat", sans-serif; font-weight: 500; color: var(--brand-blue);
    text-transform: uppercase; letter-spacing: 0.8px;
  }

  /* Spine */
  .spine-title, .spine-author {
    position: absolute; left: 0; width: 22px;
    writing-mode: vertical-rl; color: var(--paper);
    font-family: "Montserrat", sans-serif; text-transform: uppercase;
    display: flex; align-items: center; justify-content: center;
    white-space: nowrap;
  }
  .spine-title { top: 126px; height: 380px; font-weight: 500; font-size: 12px; letter-spacing: 3px; }
  .spine-author { top: 556px; height: 150px; font-weight: 700; font-size: 12px; letter-spacing: 0.8px; }

  /* Front cover */
  .front-title {
    position: absolute; left: 0; top: 44px; width: 100%;
    font-family: "Anton", sans-serif; color: var(--brand-blue);
    font-size: 66px; line-height: 86px; text-transform: uppercase; text-align: center;
    letter-spacing: 1px; white-space: nowrap;
  }
  .crowd-art {
    position: absolute; left: 88px; top: 280px; width: 350px; height: 340px;
    border-radius: 40px;
    background: radial-gradient(ellipse at 55% 60%, #ffffff 28%, var(--crowd-warm) 48%, var(--crowd-cool) 66%, rgba(255,255,255,0) 74%);
  }
  .front-tagline {
    position: absolute; left: 214px; top: 459px; width: 200px;
    font-family: "Anton", sans-serif; color: var(--tag-gray);
    font-size: 19px; line-height: 23px; text-transform: uppercase; text-align: center;
    letter-spacing: 0.3px;
  }
  .front-author {
    position: absolute; left: 0; top: 715px; width: 100%;
    font-family: "Anton", sans-serif; color: var(--brand-blue);
    font-size: 50px; line-height: 60px; text-transform: uppercase; text-align: center;
    letter-spacing: 1px; white-space: nowrap;
  }
</style>
</head>
<body>
  <main class="wrap">
    <section class="back-cover">
      <div class="back-mark" role="img" aria-label="Small aerial photo of a crowd of people standing together in an approval gesture shape"></div>
      <h2 class="back-title">Folding Waves<br>Toward Harvests</h2>
      <p class="back-tagline">A Complete Handbook For Growing Your<br>Direct Selling Venture Through Online Channels</p>
      <div class="blurb">
        <p>Folding Waves Toward Harvests is a book unlike any other you have read before. Inside you will find the exact steps to take to grow your social media following, build influence, have more appointments than ever before, and create an organisation that one day can set you free. This no nonsense guide has the potential to completely revolutionise your business, allowing you to truly create a work from anywhere you want lifestyle.</p>
        <p>The time has come to raise the professionalism of Direct Selling done on Social Media, and Folding Waves Toward Harvests is your one stop shop to achieve this!</p>
      </div>
      <h3 class="about-heading">About the Author</h3>
      <div class="author-bio">
        <div class="author-photo" role="img" aria-label="Portrait photo of the author"></div>
        <p><span class="name">Dorian Halvette</span> is a second generation Network Marketer. Having attended his first event in 1987 he has been a part of the industry ever since. After building a successful team of over 300,000 customers Dorian went into the coaching, speaking and consultancy space for the industry. He has now helped over 150,000 Network Marketers with their social media strategy, spoken on stages all over the world and worked closely with companies move into the online space.</p>
      </div>
    </section>

    <aside class="spine">
      <span class="spine-title">Folding Waves Toward Harvests</span>
      <span class="spine-author">Dorian Halvette</span>
    </aside>

    <section class="front-cover">
      <h1 class="front-title">Folding Waves<br>Toward Harvests</h1>
      <div class="crowd-art" role="img" aria-label="Aerial photo of a large crowd of people standing together to form an approval gesture shape, with scattered walkers around it"></div>
      <p class="front-tagline">A Complete Handbook For Growing Your Direct Selling Venture Through Online Channels</p>
      <p class="front-author">Dorian Halvette</p>
    </section>
  </main>
</body>
</html>
```